CD Cover Design for Groundbreaking Album

Artist: Nandi Korowe
Title: Kettles, Ribbons & Lanterns
Label: Vesh 41 Broadcasting (Indie)
We need a cover design for Nandi Korowe's sophomore music album. The title is Kettles, Ribbons & Lanterns - a follow up to Pale Harbour released in 2006.
Nandi is one of Africa's most recognizable voices. This album features Hip Hop songs laced with African rhythms performed by Nandi with a number of featured artists.
More on the artist here:
website: www.nandikorowe.example
Link to vid (artist discussing the album): http://www.vidtrove.example/watch?v=Qz4KpLm7rTa
Artist interview: http://vtrv.example/h3XaP8k_LWe

```html
<!DOCTYPE html>
<html lang="en">
<head>
<meta charset="utf-8">
<title>Kettles, Ribbons &amp; Lanterns — Nandi Korowe</title>
<link rel="stylesheet" href="https://fonts.googleapis.com/css2?family=Cabin+Sketch:wght@700&family=Raleway:wght@300&family=Cinzel:wght@400&family=Arimo:wght@400&display=swap">
<style>
  :root {
    --backdrop: #ffffff;
    --sky-top: #3b424c;
    --sky-mid: #7e838a;
    --sky-low: #c4c3bf;
    --ground: #47433f;
    --ground-deep: #2f2c2a;
    --brick: rgba(122, 72, 56, 0.75);
    --steel: rgba(150, 150, 148, 0.7);
    --figure-tone: rgba(34, 40, 58, 0.55);
    --disc-light: #ebe8e2;
    --disc-mid: #a8a49b;
    --disc-dark: #6e6b64;
    --disc-shade: rgba(78, 80, 72, 0.8);
    --ink-dark: #2a2a2a;
    --ink-light: #ffffff;
    --hub-ring: #d8dadd;
    --hub-hole: #ffffff;
    --name-top: #f4f4f4;
    --name-bottom: #8d8d8d;
  }
  * { margin: 0; padding: 0; box-sizing: border-box; }
  html, body { width: 1200px; height: 900px; overflow: hidden; background: var(--backdrop); }
  .canvas { position: relative; width: 1200px; height: 900px; }

  /* ---------- Front cover ---------- */
  .cover {
    position: absolute; left: 560px; top: 22px; width: 600px; height: 852px;
    overflow: hidden;
  }
  .cover-photo {
    position: absolute; inset: 0;
    background:
      radial-gradient(ellipse 9% 30% at 52% 72%, var(--figure-tone), transparent 100%),
      radial-gradient(ellipse 22% 28% at 6% 70%, var(--brick), transparent 100%),
      radial-gradient(ellipse 24% 30% at 90% 62%, var(--steel), transparent 100%),
      linear-gradient(180deg, var(--sky-top) 0%, var(--sky-mid) 30%, var(--sky-low) 52%, var(--sky-mid) 72%, var(--ground) 84%, var(--ground-deep) 100%);
  }
  .cover-title {
    position: absolute; left: 0; width: 100%; text-align: center;
    font-family: "Cabin Sketch", cursive; font-weight: 700; color: var(--ink-light);
    line-height: 1;
  }
  .cover-title .line-one { position: absolute; left: 0; width: 100%; top: 50px; font-size: 64px; }
  .cover-title .line-two { position: absolute; left: 0; width: 100%; top: 128px; font-size: 64px; }
  .amp { font-family: "Raleway", sans-serif; font-weight: 300; }
  .cover-label {
    position: absolute; left: 0; width: 100%; top: 212px; text-align: center;
    font-family: "Raleway", sans-serif; font-weight: 300; font-size: 25px; color: var(--ink-light);
  }
  .cover-artist {
    position: absolute; left: 0; width: 100%; top: 676px; text-align: center;
    font-family: "Cinzel", serif; font-size: 60px; letter-spacing: 1px;
    background: linear-gradient(180deg, var(--name-top), var(--name-bottom));
    -webkit-background-clip: text; background-clip: text; color: transparent;
  }

  /* ---------- Disc label ---------- */
  .disc {
    position: absolute; left: 12px; top: 300px; width: 540px; height: 540px;
    border-radius: 50%; overflow: hidden;
  }
  .disc-photo {
    position: absolute; inset: 0;
    background:
      radial-gradient(ellipse 12% 36% at 68% 78%, var(--figure-tone), transparent 100%),
      radial-gradient(ellipse 36% 30% at 20% 50%, var(--disc-shade), transparent 100%),
      linear-gradient(180deg, var(--disc-light) 0%, var(--disc-light) 30%, var(--disc-mid) 55%, var(--disc-dark) 100%);
  }
  .disc-title {
    position: absolute; left: 0; width: 100%; text-align: center;
    font-family: "Cabin Sketch", cursive; font-weight: 700; color: var(--ink-dark); line-height: 1;
  }
  .disc-title .line-one { position: absolute; left: 0; width: 100%; top: 68px; font-size: 40px; }
  .disc-title .line-two { position: absolute; left: 0; width: 100%; top: 112px; font-size: 40px; }
  .disc-blurb {
    position: absolute; left: 28px; top: 200px; width: 186px; text-align: center;
    font-family: "Arimo", sans-serif; font-size: 12px; line-height: 1.35; color: var(--ink-light);
  }
  .disc-artist {
    position: absolute; left: 380px; top: 232px; width: 140px; text-align: center;
    font-family: "Arimo", sans-serif; font-size: 21px; line-height: 1.3; color: var(--ink-dark);
  }
  .disc-label {
    position: absolute; left: 110px; top: 385px; width: 330px; text-align: center;
    font-family: "Raleway", sans-serif; font-weight: 300; font-size: 22px; line-height: 1.3; color: var(--ink-light);
  }
  .disc-hub { position: absolute; left: 220px; top: 220px; width: 100px; height: 100px; }
</style>
</head>
<body>
<main class="canvas">

  <section class="disc" aria-label="Disc label">
    <div class="disc-photo" role="img" aria-label="Photograph of the artist standing in front of pale industrial silos"></div>
    <h2 class="disc-title">
      <span class="line-one">kettles ribbons</span>
      <span class="line-two"><span class="amp">&amp;</span> lanterns</span>
    </h2>
    <p class="disc-blurb">Lorem ipsum dolor sit amet, consectetur adipiscing elit. Morbi iaculis, urna in bibendum ultrices, purus justo egestas turpis, sed tempor leo augue a augue. Cras luctus, metus id gravida blandit, lectus dui pretium est, eu volutpat elit velit vitae nisi. Proin eget nisi neque.</p>
    <p class="disc-artist">NANDI<br>KOROWE</p>
    <p class="disc-label">Vesh 41<br>Broadcasting (Indie)</p>
    <svg class="disc-hub" viewBox="0 0 100 100" aria-hidden="true">
      <circle cx="50" cy="50" r="44" fill="none" stroke="var(--hub-ring)" stroke-width="8"/>
      <circle cx="50" cy="50" r="38" fill="var(--hub-hole)"/>
    </svg>
  </section>

  <section class="cover" aria-label="Front cover">
    <div class="cover-photo" role="img" aria-label="Photograph of the artist standing in an industrial yard under a stormy sky, brick buildings and steel tanks on either side"></div>
    <h1 class="cover-title">
      <span class="line-one">kettles ribbons</span>
      <span class="line-two"><span class="amp">&amp;</span> lanterns</span>
    </h1>
    <p class="cover-label">Vesh 41 Broadcasting (Indie)</p>
    <p class="cover-artist">Nandi Korowe</p>
  </section>

</main>
</body>
</html>
```